Shabby Shic / Elegant - Web branding and elements needed

Just need a design that has all elements I will need to build out an existing template. Attaching designs that we like and want to be similar in feel to... Also attaching the barebones current template that I need to add the elements to. Anything on there can be modified, just using it for layout so you can use that as a template. In addition, feel free to play with the logo to see if there is a diffrent styl (Perhaps a more flat style).

Target Market(s)

Middle age woman, grandmothers, mothers

Industry/Entity Type

Fashion

Number of Pages Required

3 page

Font styles to use
Sans Serif
Decorative
Script

Colors

Designer to choose colors to be used in the design.

Requirements
Must have
• Easy to see. Fits with demographic.
Should not have
• Just standard, corporate feel

```html
<!DOCTYPE html>
<html lang="en">
<head>
<meta charset="utf-8">
<title>Stitchelle – Embroidery Designs</title>
<link rel="stylesheet" href="https://fonts.googleapis.com/css2?family=Open+Sans:wght@400;600;700&family=Great+Vibes&display=swap">
<style>
:root{
  --green:#6cbf45;
  --pink:#ec3a7c;
  --orange:#f47a20;
  --teal:#2c7c9c;
  --teal-dark:#1f6481;
  --ink:#222;
  --grey-bg:#efefef;
  --footer:#333;
  --footer-line:#555;
  --muted:#888;
  --white:#fff;
}
*{box-sizing:border-box;margin:0;padding:0}
html,body{width:794px;height:1200px;overflow:hidden}
body{position:relative;background:var(--white);font-family:'Open Sans',Arial,sans-serif;color:var(--ink)}
.abs{position:absolute}

/* header */
.top-nav{left:290px;top:0;width:417px;height:19px;background:var(--green);display:flex;align-items:center;padding:0 15px;gap:0}
.top-nav a{color:var(--white);font-size:6.5px;text-decoration:none;margin-right:23px;letter-spacing:.2px}
.top-nav .currency{margin-left:auto;margin-right:0;font-size:10px;font-weight:700}
.brand{left:88px;top:18px;display:flex;align-items:center;gap:6px}
.brand-dot{width:16px;height:16px;border-radius:50%;background:var(--green)}
.brand-name{font-size:27px;font-weight:700;color:var(--pink);letter-spacing:-.5px}
.search{left:290px;top:34px;width:252px;height:26px;border:1px solid #ccc;display:flex}
.search .field{flex:0 0 144px;border-right:1px solid #ddd;font-size:6px;color:#777;padding:10px 10px}
.search .dept{flex:1;font-size:6px;color:#777;padding:10px 9px}
.search .btn{width:23px;background:var(--orange);display:flex;align-items:center;justify-content:center}
.acct{top:34px;height:26px;border:1px solid #ccc;display:flex;align-items:center;padding:0 6px;gap:7px;font-size:6px;line-height:8px;color:#444}
.acct.user{left:552px;width:72px}
.acct.cart{left:635px;width:72px}
.cat-nav{left:0;top:78px;width:794px;height:20px;background:var(--pink);display:flex;justify-content:space-between;align-items:center;padding:0 18px}
.cat-nav a{color:var(--white);font-size:6.6px;text-decoration:none}

/* hero */
.hero{left:0;top:98px;width:794px;height:348px;background:linear-gradient(90deg,var(--teal-dark),var(--teal) 40%,var(--teal-dark))}
.hero-photo{left:104px;top:98px;width:280px;height:348px;background:linear-gradient(180deg,#d9c5ad,#e9eef2 45%,#8fa8c4)}
.hero-line1{left:489px;top:153px;color:var(--white);font-size:26px;font-weight:600}
.hero-line2{left:489px;top:183px;color:var(--white);font-size:25px;font-weight:400}
.hero-script{left:420px;top:196px;color:var(--white);font-family:'Great Vibes',cursive;font-size:70px}
.shop-btn{left:534px;top:287px;width:108px;height:35px;background:var(--orange);color:var(--white);font-weight:700;font-size:12.5px;display:flex;align-items:center;justify-content:center}
.dots{left:645px;top:406px;display:flex;gap:8px}
.dots span{width:6px;height:6px;border-radius:50%;background:var(--white)}
.dots span.on{background:var(--green)}

/* products */
.products{left:0;top:446px;width:794px;height:532px;background:var(--grey-bg)}
.tab{top:475px;height:26px;width:121px;font-size:8.5px;font-weight:700;display:flex;align-items:center;justify-content:center}
.tab.active{left:274px;background:var(--green);color:var(--white)}
.tab.idle{left:401px;border:1px solid #bbb;color:#333;background:var(--white)}
.card{width:149px;height:207px;background:var(--white)}
.card .art{position:absolute;left:24px;top:9px;width:101px;height:96px}
.card .badge{position:absolute;right:4px;top:4px;width:19px;height:19px;background:var(--pink);color:var(--white);font-size:5.5px;font-weight:700;line-height:6px;text-align:center;padding-top:3px}
.card .title{position:absolute;left:0;top:116px;width:100%;text-align:center;font-size:7px;line-height:9.5px}
.card .price{position:absolute;left:0;top:141px;width:100%;text-align:center}
.card .old{font-size:6.5px;color:var(--muted);text-decoration:line-through;margin-right:4px}
.card .new{font-size:13px;font-weight:700;color:var(--green)}
.card .add{position:absolute;left:40px;top:172px;width:69px;height:17px;background:var(--orange);color:var(--white);font-size:6.5px;font-weight:700;display:flex;align-items:center;justify-content:center}

/* footer */
.footer{left:0;top:978px;width:794px;height:222px;background:var(--footer)}
.foot-brand{left:88px;top:1032px;display:flex;align-items:center;gap:6px}
.foot-col{top:1016px;color:var(--white)}
.foot-col h4{font-size:6.8px;font-weight:700;margin-bottom:13px}
.foot-col a{display:block;color:#ddd;font-size:6.2px;text-decoration:none;line-height:11.6px}
.news-field{left:544px;top:1038px;width:163px;height:26px;background:#474747;color:#ccc;font-size:6px;padding:10px 10px}
.signup{left:545px;top:1072px;width:55px;height:20px;background:var(--pink);color:var(--white);font-size:8px;font-weight:700;display:flex;align-items:center;justify-content:center}
.foot-rule{left:87px;top:1132px;width:620px;height:2px;background:var(--footer-line)}
.follow{left:88px;top:1164px;color:var(--white);font-size:7px;font-weight:700}
.social{top:1158px;width:20px;height:20px;border-radius:50%}
.copy{left:500px;width:210px;text-align:right;top:1163px;color:#ddd;font-size:6.8px}
</style>
</head>
<body>

<nav class="abs top-nav">
  <a>HOME</a><a>NEW</a><a>MY ACCOUNT</a><a>BLOG</a><a>CONTACT US</a><a>FAQ</a><a class="currency">$ ▾</a>
</nav>

<div class="abs brand"><span class="brand-dot"></span><span class="brand-name">Stitchelle</span></div>

<div class="abs search">
  <div class="field">SEARCH PRODUCTS</div>
  <div class="dept">ALL DEPARTMENTS &nbsp;▾</div>
  <div class="btn"><svg width="9" height="9" viewBox="0 0 10 10"><circle cx="4" cy="4" r="3" fill="none" stroke="#fff" stroke-width="1.4"/><line x1="6.2" y1="6.2" x2="9" y2="9" stroke="#fff" stroke-width="1.6"/></svg></div>
</div>

<div class="abs acct user">
  <svg width="8" height="9" viewBox="0 0 8 9"><circle cx="4" cy="2.5" r="2.2" fill="#333"/><path d="M0 9c0-3 1.8-4.5 4-4.5S8 6 8 9z" fill="#333"/></svg>
  <div>Welcome<br>MY ACCOUNT</div>
</div>
<div class="abs acct cart">
  <svg width="10" height="9" viewBox="0 0 10 9"><path d="M0 1h2l1.3 5h5L10 2H3" fill="none" stroke="#333" stroke-width="1.2"/><circle cx="4" cy="8" r=".9" fill="#333"/><circle cx="8" cy="8" r=".9" fill="#333"/></svg>
  <div>MY CART<br>0 ITEM(S)</div>
</div>

<nav class="abs cat-nav">
  <a>NEW RELEASE</a><a>FEATURED PRODUCTS</a><a>ACCENTS</a><a>ALPHANETS &amp; LETTERING</a><a>APPLIQUE</a><a>FONT FRAMES</a><a>IN THE HOOP</a><a>WORDS &amp; PHRASES</a><a>SEWING PATTERNS</a><a>OTHER CATEGORIES</a>
</nav>

<section class="abs hero"></section>
<div class="abs hero-photo" role="img" aria-label="Photo of a smiling girl in a denim jacket over an embroidered white T-shirt"></div>
<div class="abs hero-line1">Create &amp;</div>
<div class="abs hero-line2" style="top:183px">Embellish Your</div>
<div class="abs hero-script" style="top:194px">Memories</div>
<div class="abs shop-btn">SHOP NOW</div>
<div class="abs dots"><span></span><span></span><span class="on"></span><span></span><span></span></div>

<section class="abs products"></section>
<div class="abs tab active">NEW ARRIVALS</div>
<div class="abs tab idle">FEATURED PRODUCTS</div>

<!-- row 1 -->
<div class="abs card" style="left:90px;top:527px">
  <div class="art" role="img" aria-label="Embroidery design: unicorn on roller skates with Live in Sunshine lettering" style="background:linear-gradient(135deg,#f5d6e4,#e7e2f0)"></div>
  <div class="badge">60%<br>OFF</div>
  <div class="title">LOREM IPSUM IS<br>SIMPLY DUMMY TEXT</div>
  <div class="price"><span class="old">$25.99</span><span class="new">$15.99</span></div>
  <div class="add">ADD TO CART</div>
</div>
<div class="abs card" style="left:244px;top:527px">
  <div class="art" role="img" aria-label="Embroidery design: floral Find Your Day lettering" style="background:linear-gradient(135deg,#e6f1f5,#f5ecd8)"></div>
  <div class="badge">23%<br>OFF</div>
  <div class="title">LOREM IPSUM IS<br>SIMPLY DUMMY TEXT</div>
  <div class="price"><span class="old">$25.99</span><span class="new">$15.99</span></div>
  <div class="add">ADD TO CART</div>
</div>
<div class="abs card" style="left:398px;top:527px">
  <div class="art" role="img" aria-label="Embroidery design: girl in a wreath of flowers" style="background:linear-gradient(135deg,#e4f3f4,#f7e1ea)"></div>
  <div class="title">LOREM IPSUM IS<br>SIMPLY DUMMY TEXT</div>
  <div class="price"><span class="old">$25.99</span><span class="new">$15.99</span></div>
  <div class="add">ADD TO CART</div>
</div>
<div class="abs card" style="left:553px;top:527px">
  <div class="art" role="img" aria-label="Embroidery design: Let's Ride scooter lettering" style="background:linear-gradient(135deg,#f8dbe6,#dce3f4)"></div>
  <div class="title">LOREM IPSUM IS<br>SIMPLY DUMMY TEXT</div>
  <div class="price"><span class="old">$25.99</span><span class="new">$15.99</span></div>
  <div class="add">ADD TO CART</div>
</div>

<!-- row 2 -->
<div class="abs card" style="left:90px;top:742px">
  <div class="art" role="img" aria-label="Embroidery design: Lovely Girl with butterflies" style="background:linear-gradient(135deg,#f7e1ec,#dfe4f3)"></div>
  <div class="title">LOREM IPSUM IS<br>SIMPLY DUMMY TEXT</div>
  <div class="price"><span class="old">$25.99</span><span class="new">$15.99</span></div>
  <div class="add">ADD TO CART</div>
</div>
<div class="abs card" style="left:244px;top:742px">
  <div class="art" role="img" aria-label="Embroidery design: girl holding a heart with Love lettering" style="background:linear-gradient(135deg,#ececec,#f7dbe5)"></div>
  <div class="title">LOREM IPSUM IS<br>SIMPLY DUMMY TEXT</div>
  <div class="price"><span class="old">$25.99</span><span class="new">$15.99</span></div>
  <div class="add">ADD TO CART</div>
</div>
<div class="abs card" style="left:398px;top:742px">
  <div class="art" role="img" aria-label="Embroidery design: Love Everything lettering with balloon and ice cream" style="background:linear-gradient(135deg,#f7dce5,#e9e9e9)"></div>
  <div class="badge">12%<br>OFF</div>
  <div class="title">LOREM IPSUM IS<br>SIMPLY DUMMY TEXT</div>
  <div class="price"><span class="old">$25.99</span><span class="new">$15.99</span></div>
  <div class="add">ADD TO CART</div>
</div>
<div class="abs card" style="left:553px;top:742px">
  <div class="art" role="img" aria-label="Embroidery design: Little Happy Girl lettering with rainbow" style="background:linear-gradient(135deg,#f9dbe6,#f3eee0)"></div>
  <div class="title">LOREM IPSUM IS<br>SIMPLY DUMMY TEXT</div>
  <div class="price"><span class="old">$25.99</span><span class="new">$15.99</span></div>
  <div class="add">ADD TO CART</div>
</div>

<footer class="abs footer"></footer>
<div class="abs foot-brand"><span class="brand-dot"></span><span class="brand-name">Stitchelle</span></div>
<div class="abs foot-col" style="left:314px">
  <h4>MENU</h4><a>HOME</a><a>NEW</a><a>MY ACCOUNT</a><a>BLOG</a><a>CONTACT US</a>
</div>
<div class="abs foot-col" style="left:422px">
  <h4>LINKS</h4><a>TERMS &amp; CONDITIONS</a><a>PRIVACY POLICY</a><a>FAQ</a><a>WIHSLIST</a><a>MY CART</a>
</div>
<div class="abs foot-col" style="left:543px"><h4>NEWSLETTER SIGNUP</h4></div>
<div class="abs news-field">E MAIL ID</div>
<div class="abs signup">SIGNUP</div>
<div class="abs foot-rule"></div>
<div class="abs follow">FOLLOW US</div>
<div class="abs social" style="left:145px;background:#3b5a98"></div>
<div class="abs social" style="left:169px;background:#1da1f2"></div>
<div class="abs social" style="left:194px;background:#3f729b"></div>
<div class="abs social" style="left:219px;background:#e4572e"></div>
<div class="abs social" style="left:246px;background:#0b78b5"></div>
<div class="abs copy">Copyrights @ 2017 All Rights Reserved</div>

</body>
</html>
```